Mara Joss Advisory Business Cards

Hi - using the information and logo provided I require a two sided business card designed with the following information. The business card is a 'mini card' 3.5" x 1.25".

Front of card should be the logo attached but inverted (so the background is the peach colour and the logo white).

Back should have these details. If we can't fit the Instragram and Facebook part can we just put the little logos.

Ruth Penderby

Art and Design Consultant
Dealer - Curator - Events - Styling - Creative Sourcing

P: 0462 913 058
E: ruth@marajossadvisory.example
W: www.marajossadvisory.example
I (instagram image please): marajossadvisory F (Facebook image please): MaraJossAdvisor

Target Market(s)

Galleries, artists, art buyers, interior design clients, event managers, creative types

Industry/Entity Type

Business

```html
<!DOCTYPE html>
<html lang="en">
<head>
<meta charset="utf-8">
<title>Mara Joss Advisory – Business Card</title>
<link rel="stylesheet" href="https://fonts.googleapis.com/css2?family=Arimo:wght@400;700&family=Open+Sans:wght@400&display=swap">
<style>
  :root {
    --taupe: #b78b75;
    --peach: #f3b79b;
    --peach-glow: #efb497;
    --edge: #b88a73;
    --white: #ffffff;
    --icon-ink: #c99a83;
  }
  * { margin: 0; padding: 0; box-sizing: border-box; }
  html, body { width: 1200px; height: 875px; overflow: hidden; background: var(--white); }
  .card {
    position: relative;
    width: 1200px;
    height: 875px;
    overflow: hidden;
    font-family: "Arimo", Arial, sans-serif;
    color: var(--white);
  }
  .card-front {
    position: absolute; left: 0; top: 0;
    width: 1200px; height: 429px;
    background: var(--taupe);
  }
  .front-arch { position: absolute; left: 0; top: 0; }
  .brand-dot {
    position: absolute; left: 512px; top: 48px;
    width: 176px; height: 176px; border-radius: 50%;
    background: var(--white);
  }
  .brand-name {
    position: absolute; left: 0; width: 1200px;
    text-align: center; font-weight: 400; color: var(--white);
    text-transform: uppercase; white-space: nowrap;
  }
  .brand-name--main { top: 298px; font-size: 56px; letter-spacing: 0.22em; padding-left: 0.22em; }
  .brand-name--sub { top: 384px; font-size: 30px; letter-spacing: 0.55em; padding-left: 0.55em; }
  .card-divider {
    position: absolute; left: 0; top: 429px;
    width: 1200px; height: 17px; background: var(--white);
  }
  .card-back {
    position: absolute; left: 0; top: 446px;
    width: 1200px; height: 429px;
    background: radial-gradient(ellipse 62% 78% at 50% 18%, var(--peach-glow) 0%, #dca58b 45%, var(--edge) 100%);
  }
  .person-name, .person-role, .person-services {
    position: absolute; left: 0; width: 1200px; text-align: center; white-space: nowrap;
  }
  .person-name { top: 42px; font-size: 42px; font-weight: 700; }
  .person-role { top: 101px; font-size: 30px; font-weight: 400; }
  .person-services { top: 148px; font-size: 32px; font-weight: 400; }
  .contact-rule {
    position: absolute; left: 598px; top: 200px;
    width: 3px; height: 203px; background: var(--white);
  }
  .contact-item {
    position: absolute; display: flex; align-items: center;
    font-family: "Open Sans", Arial, sans-serif; font-size: 25px; white-space: nowrap;
  }
  .contact-item--left { right: 621px; flex-direction: row; gap: 12px; }
  .contact-item--right { left: 618px; gap: 14px; }
  .contact-icon { width: 30px; height: 30px; flex: none; display: block; }
  .phone { top: 214px; }
  .email { top: 283px; }
  .web { top: 353px; }
  .social-a { top: 249px; }
  .social-b { top: 319px; }
</style>
</head>
<body>
<main class="card">
  <section class="card-front">
    <svg class="front-arch" width="1200" height="429" viewBox="0 0 1200 429" aria-hidden="true">
      <ellipse cx="600" cy="0" rx="476" ry="607" fill="var(--peach)" stroke="var(--white)" stroke-width="7"/>
    </svg>
    <div class="brand-dot" aria-hidden="true"></div>
    <p class="brand-name brand-name--main">Mara Joss</p>
    <p class="brand-name brand-name--sub">Advisory</p>
  </section>

  <div class="card-divider" aria-hidden="true"></div>

  <section class="card-back">
    <h1 class="person-name">Ruth Penderby</h1>
    <p class="person-role">Art and Design Consultant</p>
    <p class="person-services">Dealer - Curator - Events - Styling - Creative Sourcing</p>

    <div class="contact-rule" aria-hidden="true"></div>

    <p class="contact-item contact-item--left phone">
      <span>0462 913 058</span>
      <svg class="contact-icon" viewBox="0 0 30 30" aria-hidden="true">
        <circle cx="15" cy="15" r="15" fill="var(--white)"/>
        <path d="M10 7.5 l3 0.6 1 4.2 -2 1.6 q1.4 3 4.4 4.4 l1.6 -2 4.2 1 0.6 3 q-1 2.4 -3.6 2.2 q-6 -0.8 -10 -6.8 q-2 -3.4 -1.4 -6.2 q0.6 -1.8 2.2 -2z" fill="var(--icon-ink)"/>
      </svg>
    </p>
    <p class="contact-item contact-item--left email">
      <span>ruth@marajossadvisory.example</span>
      <svg class="contact-icon" viewBox="0 0 30 30" aria-hidden="true">
        <circle cx="15" cy="15" r="15" fill="var(--white)"/>
        <rect x="7" y="9.5" width="16" height="11" rx="1" fill="var(--icon-ink)"/>
        <path d="M7.5 10.5 L15 16 L22.5 10.5 M7.5 19.5 L12.5 14.8 M22.5 19.5 L17.5 14.8" fill="none" stroke="var(--white)" stroke-width="1.3"/>
      </svg>
    </p>
    <p class="contact-item contact-item--left web">
      <span>www.marajossadvisory.example</span>
      <svg class="contact-icon" viewBox="0 0 30 30" aria-hidden="true">
        <circle cx="15" cy="15" r="15" fill="var(--white)"/>
        <circle cx="13.5" cy="13.5" r="5" fill="none" stroke="var(--icon-ink)" stroke-width="2.4"/>
        <path d="M17.3 17.3 L21.5 21.5" stroke="var(--icon-ink)" stroke-width="3" stroke-linecap="round"/>
      </svg>
    </p>

    <p class="contact-item contact-item--right social-a">
      <svg class="contact-icon" viewBox="0 0 30 30" aria-hidden="true"><circle cx="15" cy="15" r="15" fill="var(--white)"/></svg>
      <span>MaraJossAdvisor</span>
    </p>
    <p class="contact-item contact-item--right social-b">
      <svg class="contact-icon" viewBox="0 0 30 30" aria-hidden="true"><circle cx="15" cy="15" r="15" fill="var(--white)"/></svg>
      <span>marajossadvisory</span>
    </p>
  </section>
</main>
</body>
</html>
```